Business Card Design job - Tyre Shop

Client wants a double sided business cards designed for a Tyre Shop.

The logo can be used in multiple ways, some examples are attached.

The reference font is:
https://www.typebarrow.com/fonts/open-sans
Others can be applied.

Color scheme should be mainly black and white, and red as a third less used color.

Contact Information for Business Card

Required Fields (Portuguese language):
- Name "Augusto Melro"
- Title "Gerente"
- Phone "253 704 862"
- Website "www.rodaslume.pt"
- Email "geral@rodaslume.pt
- Address "Rua da Fonteira N.187
4815-342 Tagilde, Vizela"

Font styles to use
Sans Serif

Requirements
Must have
• Corporate Logo
Nice to have
• The client would like the card to have special feature to measure the tyre tread, as shown in examples attached.
• The tread Values as Portuguese law are:
• - Ilegal - less than 1.6mm
• - change tyres - between 3mm and 1.6 mm
• - OK - above 3mm
• Card should be kept standard rectangle size 85x55mm

```html
<!DOCTYPE html>
<html lang="pt">
<head>
<meta charset="utf-8">
<title>Rodas Lume – Cartão de visita</title>
<link href="https://fonts.googleapis.com/css2?family=Open+Sans:wght@400;600;700;800&display=swap" rel="stylesheet">
<style>
  :root {
    --stage: #2b2b2b;
    --card: #0c0c0c;
    --white: #ffffff;
    --red: #e3262b;
    --yellow: #f2d21b;
    --soft-line: #f3c9b8;
  }
  html, body {
    margin: 0;
    padding: 0;
    width: 1200px;
    height: 1200px;
    overflow: hidden;
    background: var(--stage);
    font-family: "Open Sans", Arial, sans-serif;
  }
  .canvas {
    position: relative;
    width: 1200px;
    height: 1200px;
  }
  .card {
    position: absolute;
    left: 180px;
    width: 840px;
    height: 544px;
    background: var(--card);
    box-shadow: 0 10px 30px rgba(0,0,0,.45);
    color: var(--white);
    overflow: hidden;
  }
  .card--front { top: 40px; }
  .card--back { top: 616px; }

  .wordmark {
    position: absolute;
    display: flex;
    align-items: center;
    gap: 14px;
    font-weight: 800;
    text-transform: uppercase;
    color: var(--white);
    letter-spacing: .5px;
    line-height: 1;
  }
  .wordmark__dot {
    width: 22px;
    height: 22px;
    border-radius: 50%;
    background: var(--red);
    flex: none;
  }
  .card--front .wordmark {
    left: 0; right: 0;
    top: 220px;
    justify-content: center;
    font-size: 56px;
  }
  .front-url {
    position: absolute;
    left: 0; right: 0;
    bottom: 60px;
    text-align: center;
    color: var(--red);
    font-size: 22px;
    font-weight: 600;
    letter-spacing: .5px;
  }

  .card--back .wordmark {
    left: 48px;
    top: 62px;
    font-size: 46px;
  }
  .contact {
    position: absolute;
    right: 48px;
    top: 50px;
    text-align: right;
    font-size: 19px;
    line-height: 1.28;
  }
  .contact__name {
    font-size: 30px;
    font-weight: 700;
    letter-spacing: 1.5px;
    text-transform: uppercase;
    line-height: 1.1;
  }
  .contact__role {
    color: var(--red);
    font-size: 20px;
    font-weight: 600;
    letter-spacing: 1.5px;
    text-transform: uppercase;
    margin-bottom: 6px;
  }
  .contact__address { margin-bottom: 8px; }
  .contact__line {
    display: flex;
    justify-content: flex-end;
    align-items: center;
    gap: 10px;
  }
  .contact__line svg { width: 18px; height: 18px; flex: none; }

  .tread-legend {
    position: absolute;
    right: 48px;
    top: 290px;
    text-align: right;
    font-size: 19px;
    line-height: 1.3;
  }
  .tread-legend__title {
    text-transform: uppercase;
    letter-spacing: .5px;
  }
  .tread-legend__row {
    display: flex;
    justify-content: flex-end;
    align-items: center;
    gap: 10px;
  }
  .tread-legend__row i {
    display: inline-block;
    width: 12px;
    height: 12px;
  }
  .is-good { color: var(--white); }
  .is-good i { background: var(--white); }
  .is-change { color: var(--yellow); }
  .is-change i { background: var(--yellow); }
  .is-illegal { color: var(--red); }
  .is-illegal i { background: var(--red); }

  .tread-gauge {
    position: absolute;
    left: 0;
    top: 0;
    width: 840px;
    height: 544px;
    pointer-events: none;
  }
  .tread-gauge text {
    font-family: "Open Sans", Arial, sans-serif;
    font-size: 20px;
  }
</style>
</head>
<body>
<div class="canvas">

  <section class="card card--front" aria-label="Frente do cartão">
    <div class="wordmark"><span class="wordmark__dot"></span><span>Rodas Lume</span></div>
    <div class="front-url">www.rodaslume.pt</div>
  </section>

  <section class="card card--back" aria-label="Verso do cartão">
    <div class="wordmark"><span class="wordmark__dot"></span><span>Rodas Lume</span></div>

    <div class="contact">
      <div class="contact__name">Augusto Melro</div>
      <div class="contact__role">Gerente</div>
      <div class="contact__address">Rua da Fonteira N.187<br>4815-342 Tagilde, Vizela</div>
      <div class="contact__line">253 704 862
        <svg viewBox="0 0 24 24" aria-hidden="true"><path fill="#e3262b" d="M6.6 10.8a15 15 0 0 0 6.6 6.6l2.2-2.2c.3-.3.7-.4 1-.2 1.1.4 2.3.6 3.6.6.6 0 1 .4 1 1V20c0 .6-.4 1-1 1A17 17 0 0 1 3 4c0-.6.4-1 1-1h3.5c.6 0 1 .4 1 1 0 1.3.2 2.5.6 3.6.1.3 0 .7-.2 1z"/></svg>
      </div>
      <div class="contact__line">geral@rodaslume.pt
        <svg viewBox="0 0 24 24" aria-hidden="true"><rect x="2" y="5" width="20" height="14" fill="#e3262b"/><path d="M2 5l10 8 10-8" fill="none" stroke="#0c0c0c" stroke-width="2"/></svg>
      </div>
      <div class="contact__line">www.rodaslume.pt
        <svg viewBox="0 0 24 24" aria-hidden="true"><g fill="none" stroke="#e3262b" stroke-width="2"><circle cx="12" cy="12" r="9"/><ellipse cx="12" cy="12" rx="4" ry="9"/><path d="M3 12h18M5 7h14M5 17h14"/></g></svg>
      </div>
    </div>

    <div class="tread-legend">
      <div class="tread-legend__title">The tread values as Portuguese law are</div>
      <div class="tread-legend__row is-good">Good : above 3mm <i></i></div>
      <div class="tread-legend__row is-change">Change tyres : between 3mm and 1.6 mm <i></i></div>
      <div class="tread-legend__row is-illegal">Ilegal : less than 1.6mm <i></i></div>
    </div>

    <svg class="tread-gauge" viewBox="0 0 840 544" aria-label="Medidor de piso do pneu">
      <!-- guide lines -->
      <polyline points="0,432 710,515 840,530" fill="none" stroke="var(--red)" stroke-width="2"/>
      <polyline points="0,420 570,486 710,515" fill="none" stroke="var(--yellow)" stroke-width="2"/>
      <line x1="0" y1="370" x2="570" y2="486" stroke="var(--white)" stroke-width="1.6"/>
      <line x1="570" y1="486" x2="710" y2="515" stroke="var(--soft-line)" stroke-width="1.6"/>

      <!-- ticks -->
      <g stroke="var(--white)" stroke-width="2">
        <line x1="70" y1="355" x2="70" y2="420"/>
        <line x1="170" y1="375" x2="170" y2="440"/>
        <line x1="270" y1="395" x2="270" y2="460"/>
        <line x1="370" y1="415" x2="370" y2="480"/>
        <line x1="470" y1="435" x2="470" y2="500"/>
        <line x1="670" y1="480" x2="670" y2="530"/>
        <line x1="770" y1="505" x2="770" y2="540"/>
      </g>
      <line x1="570" y1="466" x2="570" y2="520" stroke="var(--yellow)" stroke-width="2"/>
      <line x1="710" y1="465" x2="710" y2="540" stroke="var(--red)" stroke-width="2"/>

      <!-- numbers -->
      <g fill="var(--white)" text-anchor="middle">
        <text x="70" y="344">8</text>
        <text x="170" y="364">7</text>
        <text x="270" y="384">6</text>
        <text x="370" y="404">5</text>
        <text x="470" y="424">4</text>
        <text x="570" y="462">3</text>
        <text x="670" y="470">2</text>
        <text x="770" y="496">1</text>
        <text x="70" y="318">8mm</text>
      </g>
      <line x1="70" y1="324" x2="70" y2="330" stroke="var(--white)" stroke-width="1.5"/>
      <text x="570" y="436" fill="var(--yellow)" text-anchor="middle">3mm</text>
      <line x1="570" y1="442" x2="570" y2="447" stroke="var(--yellow)" stroke-width="1.5"/>
      <text x="735" y="455" fill="var(--red)" text-anchor="middle">1.6mm</text>
    </svg>
  </section>

</div>
</body>
</html>
```